CEO of company needs clear business card that stands out from the rest

I need a clear business card (standard credit card size) for the CEO/Founder of our company...Brightfield Counseling. We would like to see designs that use our logo colors, which are khaki, chocolate brown, and gray. The card should be an edgy design, maybe where half the card is transparent with curves on the card, or a textured card where the logo is transparent, I don't care much for white cards. The final design should communicate a funky, edgy, and modern look, as well as stand out to have the "WOW" factor. The information we need on the card would be Name, Title, Toll free number, Phone Number, address, email address, and website.

*PLEASE SEND FRONT AND BACK OF CARDS

Card is two sided front and back please give us your front and back designs

The card should be an edgy design, maybe where half the card is transparent with curves on the card, or a textured card where the logo is transparent, I don't care much for white cards. The final design should communicate a funky, edgy, and modern look, as well as stand out to have the "WOW" factor.

Please follow these guidelines for the card

SPECS (card):

2.125 (h) x 3.375 (w) card size after cut

2.375 (h) x 3.625 (w) card with bleed

300 dpi

cmyk

1/8 bleed

allow 1/8 border for live area

I will also attached the pdf for the information listed above which includes a diagram of the card

 

All the cards need to have rounded edges

I just updated a card as an example of how you can use different fonts on a single business card, look how the name is written in script, so what I am saying is make this a card you will be proud to design and put it in your portfolio 

Reason: this race is really close and I am working with 2 designers to fine tune their designs and the weekend is slowing us down

• Our Logo
MUST HAVE PARTS OF CARD THAT ARE TRANSPARENT. See ideas that are attached.
Card is two sided front and back
• The final design should communicate a funky, edgy, and modern look, as well as stand out to have the "WOW" factor. The information we need on the card would be Name, Title, Toll free number, Phone Number, address, email address, and website.

```html
<!DOCTYPE html>
<html lang="en">
<head>
<meta charset="utf-8">
<title>Brightfield Counseling – Business Card Front and Back</title>
<link rel="stylesheet" href="https://fonts.googleapis.com/css2?family=Didact+Gothic&display=swap">
<style>
  :root {
    --stage: #e6e5dc;
    --card: #ffffff;
    --card-edge: #d9d8cf;
    --khaki: #8a8a3c;
    --khaki-light: #b9b874;
    --chocolate: #7a3f1c;
    --gray: #9a9a96;
    --gray-light: #d4d4cf;
    --ink: #55554f;
    --ink-soft: #7d7d76;
  }
  * { box-sizing: border-box; margin: 0; padding: 0; }
  html, body {
    width: 1200px; height: 960px; overflow: hidden;
    background: var(--stage);
    font-family: "Didact Gothic", "Century Gothic", sans-serif;
  }
  .stage { position: relative; width: 1200px; height: 960px; }
  .card {
    position: absolute; left: 280px;
    width: 640px; height: 404px;
    background: var(--card);
    border: 1px solid var(--card-edge);
    border-radius: 16px;
    overflow: hidden;
  }
  .card--front { top: 60px; }
  .card--back { top: 496px; }
  .card__band { position: absolute; inset: 0; width: 100%; height: 100%; }

  .brand-mark-area {
    position: absolute; width: 170px; height: 190px;
    border-radius: 50% 50% 45% 45%;
    background: radial-gradient(circle at 45% 40%, var(--khaki-light), var(--khaki) 75%);
    opacity: 0.85;
  }
  .card--front .brand-mark-area { left: 36px; top: 40px; }
  .card--back .brand-mark-area { left: 400px; top: 70px; }

  .wordmark {
    position: absolute; left: 356px; top: 254px;
    display: flex; align-items: center; gap: 10px;
  }
  .wordmark__dot {
    width: 22px; height: 22px; border-radius: 50%;
    background: var(--khaki);
  }
  .wordmark__name {
    font-size: 23px; line-height: 1; color: var(--chocolate);
  }
  .tagline {
    position: absolute; left: 388px; top: 288px;
    font-size: 12px; color: var(--chocolate); letter-spacing: 0.3px;
  }

  .contact { position: absolute; left: 24px; top: 178px; color: var(--ink); }
  .contact__name { font-size: 28px; font-weight: 400; line-height: 1.1; color: var(--ink); }
  .contact__title { font-size: 9px; color: var(--ink-soft); margin-top: 2px; text-transform: lowercase; }
  .contact__address { margin-top: 22px; font-size: 9.5px; line-height: 1.45; color: var(--ink-soft); }
  .contact__lines { margin-top: 10px; font-size: 9.5px; line-height: 1.45; color: var(--ink-soft); }
  .contact__lines dt { display: inline-block; width: 50px; }
  .contact__lines dd { display: inline; }
  .contact__web {
    position: absolute; left: 24px; top: 352px;
    font-size: 10px; color: var(--ink);
  }
</style>
</head>
<body>
<main class="stage">

  <section class="card card--front" aria-label="Card front">
    <svg class="card__band" viewBox="0 0 640 404" aria-hidden="true">
      <defs>
        <linearGradient id="bandFront" x1="0" y1="0" x2="1" y2="0">
          <stop offset="0" stop-color="var(--gray-light)"/>
          <stop offset="0.45" stop-color="var(--khaki-light)"/>
          <stop offset="1" stop-color="var(--chocolate)"/>
        </linearGradient>
      </defs>
    </svg>
    <svg class="card__band" viewBox="0 0 640 404" role="img" aria-label="Diagonal band of stripes in gray, khaki and brown">
      <polygon points="306,0 403,0 264,404 139,404" fill="url(#bandFront)" opacity="0.75"/>
    </svg>
    <div class="brand-mark-area" role="img" aria-label="Brand symbol decoration in khaki"></div>
    <div class="wordmark">
      <span class="wordmark__dot"></span>
      <span class="wordmark__name">Brightfield Counseling</span>
    </div>
    <p class="tagline">a pro-active addiction center</p>
  </section>

  <section class="card card--back" aria-label="Card back">
    <svg class="card__band" viewBox="0 0 640 404" role="img" aria-label="Diagonal band of stripes in gray, khaki and brown">
      <defs>
        <linearGradient id="bandBack" x1="0" y1="0" x2="1" y2="0">
          <stop offset="0" stop-color="var(--chocolate)"/>
          <stop offset="0.55" stop-color="var(--khaki-light)"/>
          <stop offset="1" stop-color="var(--gray-light)"/>
        </linearGradient>
      </defs>
      <polygon points="231,0 334,0 431,404 334,404" fill="url(#bandBack)" opacity="0.75"/>
    </svg>
    <div class="brand-mark-area" role="img" aria-label="Brand symbol decoration in khaki"></div>
    <div class="contact">
      <h1 class="contact__name">Daniel Reyes</h1>
      <p class="contact__title">CEO</p>
      <p class="contact__address">your complete address here<br>your complete address here</p>
      <dl class="contact__lines">
        <div><dt>toll free:</dt><dd>1.000.000.0000</dd></div>
        <div><dt>phone:</dt><dd>000.000.0000</dd></div>
        <div><dd>info@brightfieldcounseling.com</dd></div>
      </dl>
    </div>
    <p class="contact__web">www.brightfieldcounseling.com</p>
  </section>

</main>
</body>
</html>
```